Business Card

We need some ideas for corporate business cards. I'm interested in a double sided card, with one side featuring our corporate logo, the other side with employee information.

Corporate colors, logo etc. available at www.brivalo.com

Industry/Entity Type

Business

Requirements
Must have
• The "Brivalo" logo with stylized "O"

Nice to have
• Preferred font is calibri

```html
<!DOCTYPE html>
<html lang="en">
<head>
<meta charset="utf-8">
<title>Brivalo Business Card</title>
<link rel="stylesheet" href="https://fonts.googleapis.com/css2?family=Carlito:wght@400;700&family=Open+Sans:wght@400;800&display=swap">
<style>
  :root {
    --backdrop: #c5ced6;
    --ink: #222022;
    --teal: #0e6b70;
    --paper: #ffffff;
    --card-w: 700px;
    --card-h: 400px;
  }
  * { margin: 0; padding: 0; box-sizing: border-box; }
  html, body {
    width: 1200px;
    height: 900px;
    overflow: hidden;
    background: var(--backdrop);
  }
  .sheet {
    width: 1200px;
    height: 900px;
    display: flex;
    flex-direction: column;
    align-items: center;
    justify-content: center;
    gap: 40px;
  }
  .card {
    position: relative;
    width: var(--card-w);
    height: var(--card-h);
    background: var(--ink);
    overflow: hidden;
    box-shadow: 0 6px 18px rgba(40, 55, 70, 0.18);
  }
  .card-shapes {
    position: absolute;
    inset: 0;
    width: 100%;
    height: 100%;
  }
  .card-shapes .band { fill: var(--teal); }

  /* Front side */
  .brand {
    position: absolute;
    left: 230px;
    top: 150px;
    display: flex;
    align-items: center;
    gap: 16px;
  }
  .brand-square {
    width: 30px;
    height: 30px;
    background: var(--paper);
  }
  .brand-name {
    font-family: "Open Sans", sans-serif;
    font-weight: 800;
    font-size: 46px;
    letter-spacing: 8px;
    color: var(--paper);
    line-height: 1;
  }

  /* Back side */
  .contact-list {
    position: absolute;
    left: 470px;
    top: 38px;
    list-style: none;
    display: flex;
    flex-direction: column;
    gap: 14px;
  }
  .contact-item {
    display: flex;
    align-items: center;
    gap: 14px;
    font-family: "Carlito", "Calibri", sans-serif;
    font-size: 16px;
    color: var(--paper);
    letter-spacing: 0.3px;
  }
  .contact-icon {
    width: 20px;
    height: 20px;
    flex: none;
  }
  .identity {
    position: absolute;
    left: 60px;
    top: 270px;
    color: var(--paper);
  }
  .person-name {
    font-family: "Open Sans", sans-serif;
    font-weight: 800;
    font-size: 36px;
    letter-spacing: 2px;
    line-height: 1.05;
  }
  .person-role {
    font-family: "Open Sans", sans-serif;
    font-weight: 400;
    font-size: 18px;
    letter-spacing: 1.5px;
    margin-left: 70px;
  }
</style>
</head>
<body>
<main class="sheet">

  <section class="card card-front" aria-label="Card front">
    <svg class="card-shapes" viewBox="0 0 700 400" preserveAspectRatio="none" aria-hidden="true">
      <polygon class="band" points="0,0 260,0 0,90"/>
      <polygon class="band" points="40,400 700,400 700,150"/>
    </svg>
    <div class="brand">
      <span class="brand-square"></span>
      <span class="brand-name">BRIVALO</span>
    </div>
  </section>

  <section class="card card-back" aria-label="Card back">
    <svg class="card-shapes" viewBox="0 0 700 400" preserveAspectRatio="none" aria-hidden="true">
      <polygon class="band" points="200,0 700,0 700,330"/>
    </svg>

    <ul class="contact-list">
      <li class="contact-item">
        <svg class="contact-icon" viewBox="0 0 24 24" fill="none" stroke="#fff" stroke-width="2">
          <path d="M12 22s7-7.2 7-12.5A7 7 0 0 0 5 9.5C5 14.8 12 22 12 22z"/>
          <circle cx="12" cy="9.5" r="2.6"/>
        </svg>
        <span>123, Street name, Country</span>
      </li>
      <li class="contact-item">
        <svg class="contact-icon" viewBox="0 0 24 24" fill="#fff">
          <path d="M6.6 10.8a15.1 15.1 0 0 0 6.6 6.6l2.2-2.2a1 1 0 0 1 1-.25 11.4 11.4 0 0 0 3.6.57 1 1 0 0 1 1 1V20a1 1 0 0 1-1 1A17 17 0 0 1 3 4a1 1 0 0 1 1-1h3.5a1 1 0 0 1 1 1c0 1.25.2 2.45.57 3.57a1 1 0 0 1-.25 1z"/>
        </svg>
        <span>+852 555 0148</span>
      </li>
      <li class="contact-item">
        <svg class="contact-icon" viewBox="0 0 24 24" fill="none" stroke="#fff" stroke-width="1.8">
          <rect x="2.5" y="5" width="19" height="14"/>
          <path d="M2.5 5l9.5 8 9.5-8M2.5 19l7-6.5M21.5 19l-7-6.5"/>
        </svg>
        <span>email@brivalo.com</span>
      </li>
      <li class="contact-item">
        <svg class="contact-icon" viewBox="0 0 24 24" fill="none" stroke="#fff" stroke-width="1.8">
          <circle cx="12" cy="12" r="9.5"/>
          <path d="M2.5 12h19M12 2.5c3 3 3 16 0 19M12 2.5c-3 3-3 16 0 19"/>
        </svg>
        <span>www.brivalo.com</span>
      </li>
    </ul>

    <div class="identity">
      <p class="person-name">NAME HERE</p>
      <p class="person-role">POSITION/CEO</p>
    </div>
  </section>

</main>
</body>
</html>
```